Fernvale Craft Works business card design- Fine Art sculpture business (Contract guaranteed)

This business card is for a fine art business. Though we don't have a website up and running yet it should be up soon. I would like the business card to be elegant and fairly simple with a picture of one of my sculptures on the front (you might need to photoshop out the background) as well as my basic contact info (my name,phone # and e-mail). On the back I'd like it to be pretty simple with just "Notes" and some blank lines for writing in info.

Target Market(s)

High end artwork buyers

Industry/Entity Type

Art Gallery

Contact Information for Business Card

Marlo Prewitt Phone: (555) 213-4098 E-mail: marlo@quillbrookmail.com Facebook: @fernvalecraftworks Instagram: fernvalecraftworks

Colors

Designer to choose colors to be used in the design.

Requirements
Must have
• *A picture of one of my sculptures*, my name, business name (Fernvale Craft Works), e-mail, phone #, and a notes section on the back.
• Fernvale Craft Works
• Marlo Prewitt
• (555)213-4098
• marlo@quillbrookmail.com
• Facebook: @fernvalecraftworks
• Instagram: fernvalecraftworks
Nice to have
• It'd be nice if you can crop out the background in the sculpture pictures, which ever one you end up using.

```html
<!DOCTYPE html>
<html lang="en">
<head>
<meta charset="utf-8">
<title>Fernvale Craft Works – Business Card</title>
<link rel="stylesheet" href="https://fonts.googleapis.com/css2?family=Josefin+Sans:wght@300;400&family=Lato:wght@400&display=swap">
<style>
  :root {
    --page: #ecebe8;
    --card: #ffffff;
    --mint: #dcebe6;
    --accent: #1fa67a;
    --photo-dark: #1d5a40;
    --photo-light: #4f9a78;
    --rule: #5a5a5a;
    --ink: #333333;
  }
  html, body {
    margin: 0;
    width: 1200px;
    height: 1200px;
    overflow: hidden;
    background: var(--page);
  }
  .sheet {
    position: relative;
    width: 1200px;
    height: 1200px;
  }
  .card {
    position: absolute;
    left: 160px;
    width: 880px;
    height: 503px;
    background: var(--card);
    box-shadow: 0 6px 18px rgba(0,0,0,.15);
    overflow: hidden;
  }
  .card--front { top: 70px; }
  .card--back  { top: 627px; }
  .card svg { display: block; width: 880px; height: 503px; }
  .name {
    font-family: "Josefin Sans", sans-serif;
    font-weight: 400;
    font-size: 38px;
    fill: var(--ink);
  }
  .contact {
    font-family: "Lato", sans-serif;
    font-size: 22px;
    letter-spacing: .5px;
    fill: var(--ink);
  }
  .notes-title {
    font-family: "Josefin Sans", sans-serif;
    font-weight: 400;
    font-size: 36px;
    fill: var(--ink);
  }
</style>
</head>
<body>
<main class="sheet">

  <section class="card card--front" aria-label="Business card front">
    <svg viewBox="0 0 880 503" xmlns="http://www.w3.org/2000/svg">
      <defs>
        <linearGradient id="photoTone" x1="0" y1="0" x2="0" y2="1">
          <stop offset="0" stop-color="var(--photo-dark)"/>
          <stop offset="1" stop-color="var(--photo-light)"/>
        </linearGradient>
      </defs>

      <polygon class="mint-field" fill="var(--mint)" points="0,40 100,40 100,200 560,300 420,503 0,503"/>

      <g class="frame frame--grey" fill="none" stroke="var(--rule)" stroke-width="1.5">
        <path d="M430 40 H840 V463 H400"/>
        <rect x="826" y="34" width="14" height="14" fill="var(--card)"/>
        <rect x="826" y="449" width="14" height="14" fill="var(--card)"/>
      </g>
      <g class="frame frame--green" fill="none" stroke="var(--accent)" stroke-width="1.5">
        <path d="M400 463 H40 V70 H90"/>
        <rect x="48" y="78" width="14" height="14"/>
        <rect x="48" y="440" width="14" height="14"/>
      </g>

      <rect class="sculpture-photo" role="img" aria-label="Photograph of the artist's polished green stone sculpture"
            x="75" y="0" width="375" height="503" fill="url(#photoTone)"/>

      <text class="name" x="480" y="140">Marlo Prewitt</text>

      <g class="contact-icons" fill="none" stroke="var(--accent)" stroke-width="1.6" stroke-linecap="round">
        <path d="M496 254 c2 8 8 14 16 16 l3-4 -5-3 -3 2 c-3-1-5-4-6-6 l2-3 -3-5 z"/>
        <circle cx="505" cy="310" r="4"/>
        <path d="M509 310 v3 c0 3 5 3 5-2 a9 9 0 1 0 -4 8"/>
        <circle cx="505" cy="357" r="7"/>
      </g>

      <text class="contact" x="540" y="268">(555) 213-4098</text>
      <text class="contact" x="540" y="318">marlo@quillbrookmail.com</text>
      <text class="contact" x="540" y="365">@fernvalecraftworks</text>
    </svg>
  </section>

  <section class="card card--back" aria-label="Business card back">
    <svg viewBox="0 0 880 503" xmlns="http://www.w3.org/2000/svg">
      <defs>
        <clipPath id="mintArea">
          <polygon points="0,0 300,0 480,300 300,503 0,503"/>
        </clipPath>
      </defs>

      <polygon class="mint-field" fill="var(--mint)" points="0,0 300,0 480,300 300,503 0,503"/>

      <g class="frame frame--grey" fill="none" stroke="var(--rule)" stroke-width="1.5">
        <path d="M370 40 H40 V463 H840 V40 H510"/>
        <rect x="826" y="54" width="14" height="14" fill="var(--card)"/>
        <rect x="826" y="449" width="14" height="14" fill="var(--card)"/>
      </g>
      <g class="frame frame--green" fill="none" stroke="var(--accent)" stroke-width="1.5" clip-path="url(#mintArea)">
        <path d="M370 40 H40 V463 H840"/>
        <rect x="48" y="425" width="14" height="14"/>
      </g>

      <text class="notes-title" x="440" y="54" text-anchor="middle">Notes</text>

      <g class="writing-lines writing-lines--grey" stroke="var(--rule)" stroke-width="1.3">
        <line x1="80" y1="100" x2="800" y2="100"/>
        <line x1="80" y1="150" x2="800" y2="150"/>
        <line x1="80" y1="200" x2="800" y2="200"/>
        <line x1="80" y1="250" x2="800" y2="250"/>
        <line x1="80" y1="300" x2="800" y2="300"/>
        <line x1="80" y1="350" x2="800" y2="350"/>
        <line x1="80" y1="400" x2="800" y2="400"/>
      </g>
      <g class="writing-lines writing-lines--green" stroke="var(--accent)" stroke-width="1.3" clip-path="url(#mintArea)">
        <line x1="80" y1="100" x2="800" y2="100"/>
        <line x1="80" y1="150" x2="800" y2="150"/>
        <line x1="80" y1="200" x2="800" y2="200"/>
        <line x1="80" y1="250" x2="800" y2="250"/>
        <line x1="80" y1="300" x2="800" y2="300"/>
        <line x1="80" y1="350" x2="800" y2="350"/>
        <line x1="80" y1="400" x2="800" y2="400"/>
      </g>
    </svg>
  </section>

</main>
</body>
</html>
```